Our company needs a Corporate Identity Package!!!

We would like to receive submissions for a corporate identity pachage including the following elements:

1. Presentation Folder
2. Product/Service Catalogue (16 A4 pages landscape but expandable)
3. Product Brochure (up to 8 A4 pages)
4. Product Flyer (2 A4 pages)
5. Business Card
6. Letterhead
7. Envelope
8. E-mail signature.

I attach a Presentation Folder that i like (geometric but also has circle). We would like to have some ideas regarding the above 7 elements including brintavex logo colors (brintavex.example).

Payment is indicative and we are planning to increase the payment now that we found out how to actually do this. You are also more than welcome to send us a message and suggest the amount of payment for your Corporate Identity elements and we will update this.

Target Market(s)

Home | Office | Life

Colors
f78f20
0555a3
9bcb3b

Requirements
Must have
• 1. Presentation Folder
• 2. Product/Service Catalogue (16 A4 pages landscape but to be easily expandable)
• 3. Product Brochure (up to 4 A4 pages but to be easily expandable )
• 4. Product Flyer (2 A4 pages)
• 5. Business Card
• 6. Letterhead
• 7. Envelope
• 8. E-mail signature.
Nice to have
• It would be nice to include design something around the cycle that communicates the best six doctors (i.e. sunshine, water, rest, air, exercise and diet) !!!

```html
<!DOCTYPE html>
<html lang="en">
<head>
<meta charset="utf-8">
<title>brintavex business card</title>
<link href="https://fonts.googleapis.com/css2?family=Open+Sans:wght@400;600&display=swap" rel="stylesheet">
<style>
  :root {
    --bg: #e9edf0;
    --paper: #ffffff;
    --navy: #0d1a33;
    --blue: #0555a3;
    --orange: #f78f20;
    --green: #9bcb3b;
    --lime: #c9dc3a;
    --text: #3b4350;
    --muted: #7b8592;
  }
  * { margin: 0; padding: 0; box-sizing: border-box; }
  html, body { width: 1200px; height: 913px; overflow: hidden; }
  body {
    background: var(--bg);
    font-family: "Open Sans", Arial, sans-serif;
    position: relative;
  }
  .card {
    position: absolute;
    top: 308px;
    width: 520px;
    height: 297px;
    overflow: hidden;
    box-shadow: 0 6px 18px rgba(20, 30, 50, 0.15);
  }
  .card-front { left: 40px; background: var(--paper); }
  .card-back { left: 640px; background: var(--navy); }
  .card-art { position: absolute; inset: 0; width: 520px; height: 297px; }
  .brand {
    position: absolute;
    display: flex;
    align-items: center;
    gap: 10px;
  }
  .brand-dot {
    width: 30px; height: 30px;
    border-radius: 50%;
    background: var(--orange);
    flex: none;
  }
  .brand-name {
    font-weight: 400;
    font-size: 32px;
    line-height: 1;
    color: var(--blue);
    letter-spacing: 0.5px;
  }
  .brand-tagline {
    position: absolute;
    font-size: 7px;
    letter-spacing: 2px;
    color: var(--muted);
  }
  .card-front .brand { left: 38px; top: 128px; }
  .card-front .brand-tagline { left: 79px; top: 164px; }
  .card-back .brand { left: 150px; top: 132px; }
  .card-back .brand-name { font-size: 38px; color: #5aa8e0; }
  .card-back .brand-dot { width: 34px; height: 34px; }
  .card-back .brand-tagline { left: 196px; top: 176px; color: #8fa3bf; }
  .contact {
    position: absolute;
    left: 58px;
    top: 190px;
    list-style: none;
    font-size: 8.5px;
    line-height: 13px;
    color: var(--text);
  }
  .contact li { display: flex; align-items: flex-start; gap: 5px; }
  .contact svg { flex: none; margin-top: 2px; }
  .contact .address { padding-left: 0; margin-bottom: 2px; }
</style>
</head>
<body>

<section class="card card-front" aria-label="Business card front">
  <svg class="card-art" viewBox="0 0 520 297">
    <defs>
      <linearGradient id="front-pattern-tone" x1="0" y1="0" x2="1" y2="1">
        <stop offset="0" stop-color="#9bcb3b"/>
        <stop offset="0.35" stop-color="#2f8fd6"/>
        <stop offset="0.65" stop-color="#f78f20"/>
        <stop offset="1" stop-color="#2b3a8c"/>
      </linearGradient>
    </defs>
    <polygon role="img" aria-label="Geometric cube pattern in green, blue and orange"
      points="240,0 520,0 520,160 420,225 330,185 260,95" fill="url(#front-pattern-tone)"/>
    <polygon points="358,218 398,200 388,236" fill="var(--orange)"/>
    <polygon points="268,108 284,102 278,118" fill="var(--lime)"/>
  </svg>

  <div class="brand">
    <span class="brand-dot"></span>
    <span class="brand-name">brintavex</span>
  </div>
  <div class="brand-tagline">HOME | OFFICE | LIFE</div>

  <ul class="contact">
    <li class="address">48 Larkfield Ave, Halden<br>ON Canada K2P4R8</li>
    <li>
      <svg width="8" height="8" viewBox="0 0 8 8"><path d="M1 1 L3 1 L3.6 2.6 L2.6 3.3 Q3.5 4.8 4.7 5.4 L5.4 4.4 L7 5 L7 7 Q2 7 1 1Z" fill="var(--green)"/></svg>
      <span>555 014 2290</span>
    </li>
    <li>
      <svg width="8" height="8" viewBox="0 0 8 8"><rect x="0.5" y="1.5" width="7" height="5" fill="none" stroke="var(--green)"/><path d="M0.5 1.5 L4 4.5 L7.5 1.5" fill="none" stroke="var(--green)"/></svg>
      <span>info@brintavex.example</span>
    </li>
    <li>
      <svg width="8" height="8" viewBox="0 0 8 8"><circle cx="4" cy="4" r="3.5" fill="var(--green)"/></svg>
      <span>www.brintavex.example</span>
    </li>
  </ul>
</section>

<section class="card card-back" aria-label="Business card back">
  <svg class="card-art" viewBox="0 0 520 297">
    <defs>
      <linearGradient id="back-pattern-tone" x1="0" y1="0" x2="1" y2="1">
        <stop offset="0" stop-color="#2f8fd6"/>
        <stop offset="0.4" stop-color="#9bcb3b"/>
        <stop offset="0.75" stop-color="#f78f20"/>
        <stop offset="1" stop-color="#2b3a8c"/>
      </linearGradient>
    </defs>
    <polygon role="img" aria-label="Geometric cube pattern in blue, green and orange"
      points="350,0 520,0 520,200 455,170 400,110 360,60" fill="url(#back-pattern-tone)"/>
    <polygon points="326,72 338,66 334,80" fill="var(--green)"/>
    <polygon points="388,150 404,144 398,160" fill="var(--lime)"/>
    <polygon points="470,232 500,222 492,248" fill="var(--orange)"/>
  </svg>

  <div class="brand">
    <span class="brand-dot"></span>
    <span class="brand-name">brintavex</span>
  </div>
  <div class="brand-tagline">HOME | OFFICE | LIFE</div>
</section>

</body>
</html>
```